Retractable Banner Stands

Hello we need a deisgn for a banner.
Sizes: 36"x80", 12"x17"(this one to have less on it, most the logo, license numvber, and address), and a 24"x40" banner
Roofing Services
HOA & Commercial Roofing
• Emergency roof tarping & repairs — Starting at $550
• Small & large roof repairs
• Preventative roof maintenance
• Full roof replacement
Deck & Balcony Services
• Balcony & deck maintenance
SB-326 Repairs
• Deck resurfacing
• Small & large deck repairs
• Full deck reconstruction
Gutter Services
• Small & large gutter repairs
• Gutter cleaning & maintenance
• New gutter installation & replacement
License Information:
C-39 Roofing Contractor
General B Contractor
License #4529730
📍 Serving Orange County & Surrounding Areas
📍 Office Location:
41 Dunwick Street, Suite F
Target Market(s)
HOA & Commerical roofs
Industry/Entity Type
Roofing
Other font styles liked:
- Gotham
Look and feel

```html
<!DOCTYPE html>
<html lang="en">
<head>
<meta charset="utf-8">
<title>Kestrel Roofing &amp; Waterproofing – Roofing Services</title>
<link rel="stylesheet" href="https://fonts.googleapis.com/css2?family=Montserrat:wght@600;800&family=Roboto:wght@400;500&display=swap">
<style>
  :root {
    --bg: #eaf6fc;
    --frame: #1ab0ef;
    --accent: #12a9ee;
    --ink: #111111;
    --body: #3a3a3a;
    --house-light: #efe9dc;
    --house-dark: #3b352f;
  }
  * { margin: 0; padding: 0; box-sizing: border-box; }
  html, body { width: 720px; height: 1200px; overflow: hidden; background: var(--bg); }
  .banner {
    position: relative; width: 720px; height: 1200px; overflow: hidden;
    background: var(--bg); font-family: "Roboto", Arial, sans-serif;
  }
  .frame {
    position: absolute; left: 17px; top: 17px; width: 688px; height: 1166px;
    border: 4px solid var(--frame); z-index: 1;
  }
  .house-photo { position: absolute; left: 0; top: 0; z-index: 2; }
  .brand { position: absolute; top: 52px; left: 0; width: 720px; text-align: center; z-index: 3; }
  .brand-name {
    font-family: "Montserrat", Arial, sans-serif; font-weight: 800; font-size: 72px;
    line-height: 80px; letter-spacing: 1px; color: var(--ink);
  }
  .brand-tag {
    font-family: "Montserrat", Arial, sans-serif; font-weight: 600; font-size: 18px;
    line-height: 24px; color: var(--ink); margin-top: 12px; letter-spacing: 0.3px;
  }
  .content { position: absolute; left: 42px; top: 0; width: 640px; height: 1200px; z-index: 3; }
  .title {
    position: absolute; top: 207px; left: 0; white-space: nowrap;
    font-weight: 500; font-size: 42px; line-height: 52px; color: var(--accent);
  }
  .section-heading {
    position: absolute; left: 0; white-space: nowrap;
    font-weight: 500; font-size: 25px; line-height: 32px; color: var(--ink);
  }
  .service-list { position: absolute; left: 0; list-style: none; }
  .service-list li {
    display: flex; align-items: center; height: 37.5px; white-space: nowrap;
    font-size: 21.5px; color: var(--body);
  }
  .service-list svg { width: 20px; height: 18px; margin: 0 18px 0 4px; flex: none; }
  .license {
    position: absolute; top: 895px; left: 0; white-space: nowrap;
    font-weight: 500; font-size: 22.5px; line-height: 31px; color: var(--ink);
  }
  .license .divider { display: inline-block; margin: 0 22px; font-weight: 400; }
  .location {
    position: absolute; left: 0; width: 360px; display: flex; align-items: flex-start;
    white-space: nowrap; font-size: 21.5px; line-height: 34px; color: var(--body);
  }
  .location svg { width: 18px; height: 24px; margin: 4px 10px 0 0; flex: none; }
</style>
</head>
<body>
<div class="banner">
  <div class="frame"></div>

  <svg class="house-photo" width="720" height="1200" viewBox="0 0 720 1200" role="img" aria-label="Photo of a white board-and-batten house with dark shingle gable roofs against the sky">
    <defs>
      <linearGradient id="houseTone" x1="0" y1="0" x2="1" y2="1">
        <stop offset="0" stop-color="#3b352f"/>
        <stop offset="0.25" stop-color="#efe9dc"/>
        <stop offset="1" stop-color="#d8d0c1"/>
      </linearGradient>
    </defs>
    <path d="M333 1200 L478 972 L560 1012 L665 812 L720 838 L720 1200 Z" fill="url(#houseTone)"/>
  </svg>

  <header class="brand">
    <div class="brand-name">KESTREL</div>
    <div class="brand-tag">ROOFING &amp; WATERPROOFING</div>
  </header>

  <main class="content">
    <h1 class="title">Roofing Services</h1>

    <h2 class="section-heading" style="top:278px">HOA &amp; Commercial Roofing</h2>
    <ul class="service-list" style="top:323px">
      <li><svg viewBox="0 0 20 18"><path d="M2 2l7 7-7 7M10 2l7 7-7 7" fill="none" stroke="var(--accent)" stroke-width="2.6"/></svg>Emergency roof tarping &amp; repairs — Starting at $550</li>
      <li><svg viewBox="0 0 20 18"><path d="M2 2l7 7-7 7M10 2l7 7-7 7" fill="none" stroke="var(--accent)" stroke-width="2.6"/></svg>Small &amp; large roof repairs</li>
      <li><svg viewBox="0 0 20 18"><path d="M2 2l7 7-7 7M10 2l7 7-7 7" fill="none" stroke="var(--accent)" stroke-width="2.6"/></svg>Preventative roof maintenance</li>
      <li><svg viewBox="0 0 20 18"><path d="M2 2l7 7-7 7M10 2l7 7-7 7" fill="none" stroke="var(--accent)" stroke-width="2.6"/></svg>Full roof replacement</li>
    </ul>

    <h2 class="section-heading" style="top:489px">Deck &amp; Balcony Services</h2>
    <ul class="service-list" style="top:533px">
      <li><svg viewBox="0 0 20 18"><path d="M2 2l7 7-7 7M10 2l7 7-7 7" fill="none" stroke="var(--accent)" stroke-width="2.6"/></svg>Balcony &amp; deck maintenance SB-326 Repairs</li>
      <li><svg viewBox="0 0 20 18"><path d="M2 2l7 7-7 7M10 2l7 7-7 7" fill="none" stroke="var(--accent)" stroke-width="2.6"/></svg>Deck resurfacing</li>
      <li><svg viewBox="0 0 20 18"><path d="M2 2l7 7-7 7M10 2l7 7-7 7" fill="none" stroke="var(--accent)" stroke-width="2.6"/></svg>Small &amp; large deck repairs</li>
      <li><svg viewBox="0 0 20 18"><path d="M2 2l7 7-7 7M10 2l7 7-7 7" fill="none" stroke="var(--accent)" stroke-width="2.6"/></svg>Full deck reconstruction</li>
    </ul>

    <h2 class="section-heading" style="top:700px">Gutter Services</h2>
    <ul class="service-list" style="top:744px">
      <li><svg viewBox="0 0 20 18"><path d="M2 2l7 7-7 7M10 2l7 7-7 7" fill="none" stroke="var(--accent)" stroke-width="2.6"/></svg>Small &amp; large gutter repairs</li>
      <li><svg viewBox="0 0 20 18"><path d="M2 2l7 7-7 7M10 2l7 7-7 7" fill="none" stroke="var(--accent)" stroke-width="2.6"/></svg>Gutter cleaning &amp; maintenance</li>
      <li><svg viewBox="0 0 20 18"><path d="M2 2l7 7-7 7M10 2l7 7-7 7" fill="none" stroke="var(--accent)" stroke-width="2.6"/></svg>New gutter installation &amp; replacement</li>
    </ul>

    <p class="license">C-39 Roofing Contractor<span class="divider">|</span>General B Contractor<br>License #4529730</p>

    <p class="location" style="top:980px">
      <svg viewBox="0 0 18 24"><path d="M9 1C4.6 1 1 4.4 1 8.8 1 14.5 9 23 9 23s8-8.5 8-14.2C17 4.4 13.4 1 9 1z" fill="var(--accent)"/></svg>
      <span>Serving Orange County &amp;<br>Surrounding Areas</span>
    </p>
    <p class="location" style="top:1061px">
      <svg viewBox="0 0 18 24"><path d="M9 1C4.6 1 1 4.4 1 8.8 1 14.5 9 23 9 23s8-8.5 8-14.2C17 4.4 13.4 1 9 1z" fill="var(--accent)"/></svg>
      <span>Office Location: 41 Dunwick<br>Street, Suite F</span>
    </p>
  </main>
</div>
</body>
</html>
```